Boutique Financial Services firm require Custom Christmas Card

We are Brindle Court, a Melbourne based financial services firm that offer high quality financial solutions to our clients. We need a Christmas Card to send to our valued clients that evokes our exceptional quality, care and thoughtfulness of our bespoke financial advice.
The design must be elegant and simple, incorporating our "tree" logo and brand colour. Please have a look at our website to further understand our brand: https://brindlevq.example/. I've attached the Christmas card which was created last year for reference.
The interior of the card must include a simple message such as "Season's Greetings" or "Merry Christmas" and the back of the card must list "Contact Details: 12/71 Wexford Lane, Melbourne VIC 3000, 03 7415 3862, hello@brindlevq.example"
The new Christmas card must be formatted as per below print format:
- Spread size: 250mm x 194mm
- Finished size: 125mm x 194mm
The design must also be provided in digital formats (Facebook, Instagram) for social media posting.
Please submit a minimum of 2 design options per designer. We must confirm our card design by Thurs Dec 6 to allow time for printing & posting.
Target Market(s)
Men & women, aged 35-70, with families, own their own home, wealthy, enjoys the finer things in life. Please have a look at our website to further understand our brand: https://brindlevq.example/.
Industry/Entity Type
Financial Service
Colors
Designer to choose colors to be used in the design.
Requirements
Must have
- The design must be elegant, simple and evoke Christmas spirits. We would like our logo and brand colour incorporated somehow. I've attached our brand guidelines and the Christmas card which was created last year for your reference.
- The front & interior of the card must include a simple message such as "Season's Greetings" or "Merry Christmas" and the back of the card must list "Contact Details: Brindle Court, 12/71 Wexford Lane, Melbourne VIC 3000, 03 7415 3862, hello@brindlevq.example"
- The new Christmas card must be formatted as per below print format:
- - Spread size: 250mm x 194mm
- - Finished size: 125mm x 194mm
- The design must also be provided in digital formats (Facebook, Instagram) for social media posting.

```html
<!DOCTYPE html>
<html lang="en">
<head>
<meta charset="utf-8">
<title>Brindle Court – Christmas Card</title>
<link rel="stylesheet" href="https://fonts.googleapis.com/css2?family=Allura&family=Montserrat:wght@400;600&family=Yanone+Kaffeesatz:wght@400&display=swap">
<style>
  :root {
    --backdrop: #e9e9e9;
    --card: #ffffff;
    --brand-green: #a5b119;
    --ink: #3a3b3e;
    --ink-soft: #5c5d60;
    --band: #e8ebbd;
    --star-grey: #707173;
  }
  * { margin: 0; padding: 0; box-sizing: border-box; }
  html, body {
    width: 721px;
    height: 1200px;
    overflow: hidden;
    background: var(--backdrop);
  }
  .card {
    position: absolute;
    left: 25px;
    width: 667px;
    background: var(--card);
    box-shadow: 0 2px 6px rgba(0,0,0,0.18);
  }
  .card--outside { top: 61px; height: 519px; }
  .card--inside { top: 616px; height: 513px; }

  .snow-band {
    position: absolute;
    left: 6px;
    right: 6px;
    height: 12px;
    background: var(--band);
    border-radius: 6px;
  }
  .card--outside .snow-band { top: 495px; }
  .card--inside .snow-band { top: 490px; }

  /* Outside spread */
  .star-trail {
    position: absolute;
    left: 0;
    top: 0;
    width: 667px;
    height: 400px;
    fill: var(--star-grey);
  }
  .tree-ornament-art {
    position: absolute;
    left: 392px;
    top: 92px;
    width: 216px;
    height: 298px;
    background: radial-gradient(ellipse at 50% 36%, #c3cc55 0%, #d6dc85 38%, #ecdcc4 72%, rgba(255,255,255,0) 100%);
    border-radius: 50% 50% 30% 30% / 40% 40% 20% 20%;
  }
  .front-greeting {
    position: absolute;
    left: 412px;
    top: 424px;
    width: 176px;
    text-align: center;
    font-family: "Yanone Kaffeesatz", sans-serif;
    font-weight: 400;
    font-size: 40px;
    line-height: 40px;
    color: var(--ink);
    white-space: nowrap;
  }
  .contact-details {
    position: absolute;
    left: 86px;
    top: 428px;
    width: 160px;
    text-align: center;
    font-family: "Montserrat", sans-serif;
    font-size: 9px;
    line-height: 12px;
    color: var(--ink-soft);
    font-style: normal;
  }
  .contact-details .email {
    color: var(--brand-green);
    font-weight: 600;
  }

  /* Inside spread */
  .hanging-ornaments-art {
    position: absolute;
    left: 188px;
    top: 0;
    width: 291px;
    height: 122px;
    background: linear-gradient(180deg, rgba(230,190,170,0.35) 0%, rgba(200,215,160,0.35) 55%, rgba(255,255,255,0) 100%);
    border-radius: 0 0 50% 50% / 0 0 30% 30%;
  }
  .inside-lead {
    position: absolute;
    left: 0;
    right: 0;
    top: 165px;
    padding-right: 14px;
    text-align: center;
    font-family: "Montserrat", sans-serif;
    font-size: 20px;
    line-height: 26px;
    color: var(--ink);
  }
  .inside-greeting {
    position: absolute;
    left: 0;
    right: 0;
    top: 200px;
    padding-right: 14px;
    text-align: center;
    font-family: "Yanone Kaffeesatz", sans-serif;
    font-weight: 400;
    font-size: 104px;
    line-height: 100px;
    color: var(--brand-green);
    white-space: nowrap;
  }
  .signature {
    position: absolute;
    right: 58px;
    top: 362px;
    font-family: "Allura", cursive;
    font-size: 34px;
    line-height: 40px;
    color: var(--ink);
  }
  .signatory {
    position: absolute;
    right: 58px;
    top: 413px;
    font-family: "Montserrat", sans-serif;
    font-size: 11.5px;
    line-height: 16px;
    color: var(--ink-soft);
  }
  .brand-name {
    position: absolute;
    right: 58px;
    top: 440px;
    display: flex;
    align-items: center;
    gap: 6px;
    font-family: "Montserrat", sans-serif;
    font-weight: 600;
    font-size: 16px;
    line-height: 26px;
    color: var(--ink);
  }
  .brand-name .dot {
    width: 26px;
    height: 26px;
    border-radius: 50%;
    background: var(--brand-green);
  }
</style>
</head>
<body>

<section class="card card--outside">
  <svg class="star-trail" viewBox="0 0 667 400" aria-hidden="true">
    <defs>
      <path id="star" d="M0,-1 L0.22,-0.22 L1,0 L0.22,0.22 L0,1 L-0.22,0.22 L-1,0 L-0.22,-0.22 Z"/>
    </defs>
    <use href="#star" transform="translate(65 282) scale(7)"/>
    <use href="#star" transform="translate(108 284) scale(4.5)"/>
    <use href="#star" transform="translate(156 279) scale(4.5)"/>
    <use href="#star" transform="translate(82 321) scale(8)"/>
    <use href="#star" transform="translate(152 310) scale(4.5)"/>
    <use href="#star" transform="translate(196 297) scale(6.5)"/>
    <use href="#star" transform="translate(250 282) scale(6)"/>
    <use href="#star" transform="translate(244 324) scale(6.5)"/>
    <use href="#star" transform="translate(304 286) scale(7)"/>
    <use href="#star" transform="translate(267 241) scale(4.5)"/>
    <use href="#star" transform="translate(319 237) scale(6)"/>
    <use href="#star" transform="translate(372 209) scale(6)"/>
    <use href="#star" transform="translate(365 157) scale(6.5)"/>
    <use href="#star" transform="translate(419 89) scale(6.5)"/>
    <use href="#star" transform="translate(462 95) scale(4.5)"/>
    <use href="#star" transform="translate(506 65) scale(6)"/>
    <use href="#star" transform="translate(525 91) scale(4.5)"/>
    <use href="#star" transform="translate(568 86) scale(6.5)"/>
    <use href="#star" transform="translate(612 146) scale(6.5)"/>
    <use href="#star" transform="translate(618 200) scale(6.5)"/>
  </svg>
  <div class="tree-ornament-art" role="img" aria-label="Green leafy tree inside a circle with red and orange Christmas ornaments hanging below"></div>
  <address class="contact-details">
    12/71 Wexford Lane<br>
    Melbourne VIC 3000<br>
    03 7415 3862<br>
    <span class="email">hello@brindlevq.example</span>
  </address>
  <h1 class="front-greeting">MERRY CHRISTMAS</h1>
  <div class="snow-band" role="img" aria-label="Border of pale green snowflakes"></div>
</section>

<section class="card card--inside">
  <div class="hanging-ornaments-art" role="img" aria-label="Row of hanging Christmas ornaments in red, green and orange: stars, baubles, trees, a snowman, stocking, gift and reindeer"></div>
  <p class="inside-lead">Wishing you a</p>
  <h2 class="inside-greeting">MERRY CHRISTMAS</h2>
  <p class="signature">Rowan Hale</p>
  <p class="signatory">Rowan Hale CEO &amp; Brindle Team</p>
  <div class="brand-name"><span class="dot"></span>Brindle Court</div>
  <div class="snow-band" role="img" aria-label="Border of pale green snowflakes"></div>
</section>

</body>
</html>
```